Verostel business card

Business card for sustainable investment company called "Verostel". Verostel is an exchange platform selling carbon credits between buyers and sellers. Carbon Credits are an environmental commodity for reducing global carbon emissions.

the card should obviously have our logo and the theme should be sustainability/environment mixed with a trading platform.

Contact Information for Business Card

Logo, Name, Title, Phone, Email

Colors
0054AA
0677BA
7BADD7
CADEEF
E8F1F8
0094D4
00A9DD
6FCCEA
C7EBF8
E9F6FB
00AB8E
00BBA5
67D7C9
C6EFE9
E9F9F6
59FF00
82FF00
B8FF75
E3FFCB
F4FFEA

```html
<!DOCTYPE html>
<html lang="en">
<head>
<meta charset="utf-8">
<title>Verostel business card</title>
<link rel="stylesheet" href="https://fonts.googleapis.com/css2?family=Outfit:wght@400;500;600&display=swap">
<style>
  :root {
    --backdrop: #2b2b2b;
    --card-navy: #233655;
    --card-white: #ffffff;
    --brand-blue: #0094d4;
    --ink: #1c1c1c;
    --on-navy: #ffffff;
  }
  * { margin: 0; padding: 0; box-sizing: border-box; }
  html, body {
    width: 1200px;
    height: 900px;
    overflow: hidden;
  }
  body {
    background: var(--backdrop);
    font-family: "Outfit", sans-serif;
    position: relative;
  }
  .card {
    position: absolute;
    top: 302px;
    width: 513px;
    height: 295px;
    box-shadow: 0 6px 14px rgba(0, 0, 0, 0.45);
  }
  .card-front {
    left: 73px;
    background: var(--card-navy);
  }
  .front-texture {
    position: absolute;
    inset: 0;
    background: var(--card-navy);
  }
  .front-wordmark {
    position: absolute;
    right: 40px;
    top: 216px;
    font-size: 25px;
    font-weight: 600;
    letter-spacing: 0.3px;
    color: var(--on-navy);
  }
  .card-back {
    left: 615px;
    background: var(--card-white);
  }
  .back-wordmark {
    position: absolute;
    left: 126px;
    top: 150px;
    transform: translate(-50%, -50%);
    font-size: 27px;
    font-weight: 600;
    color: var(--brand-blue);
  }
  .divider {
    position: absolute;
    left: 240px;
    top: 57px;
    width: 2px;
    height: 183px;
    background: var(--brand-blue);
  }
  .contact {
    position: absolute;
    left: 291px;
    top: 86px;
    color: var(--ink);
  }
  .contact-name {
    font-size: 18px;
    font-weight: 500;
    line-height: 1.2;
  }
  .contact-title {
    font-size: 12px;
    font-weight: 500;
    text-transform: uppercase;
    margin-top: 3px;
  }
  .contact-lines {
    list-style: none;
    margin-top: 17px;
    font-size: 13px;
  }
  .contact-lines li {
    display: flex;
    align-items: center;
    gap: 6px;
    height: 19px;
  }
  .contact-lines svg { width: 11px; height: 11px; fill: var(--brand-blue); }
  .contact-web {
    font-size: 13px;
    margin-top: 13px;
  }
</style>
</head>
<body>
  <section class="card card-front">
    <div class="front-texture" role="img" aria-label="Subtle repeating brand mark pattern on navy"></div>
    <div class="front-wordmark">VEROSTEL</div>
  </section>

  <section class="card card-back">
    <div class="back-wordmark">VEROSTEL</div>
    <div class="divider"></div>
    <div class="contact">
      <p class="contact-name">Daniel Marlowe</p>
      <p class="contact-title">Managing Director</p>
      <ul class="contact-lines">
        <li>
          <svg viewBox="0 0 24 24" aria-hidden="true"><path d="M6.6 10.8a15.1 15.1 0 0 0 6.6 6.6l2.2-2.2a1 1 0 0 1 1-.25 11.4 11.4 0 0 0 3.6.57 1 1 0 0 1 1 1V20a1 1 0 0 1-1 1A17 17 0 0 1 3 4a1 1 0 0 1 1-1h3.5a1 1 0 0 1 1 1c0 1.25.2 2.45.57 3.57a1 1 0 0 1-.25 1z"/></svg>
          <span>5550 123 456</span>
        </li>
        <li>
          <svg viewBox="0 0 24 24" aria-hidden="true"><path d="M2 5h20v2l-10 6L2 7z"/><path d="M2 9l10 6 10-6v10H2z"/></svg>
          <span>d.marlowe@verostel.com</span>
        </li>
      </ul>
      <p class="contact-web">www.verostel.com</p>
    </div>
  </section>
</body>
</html>
```